Killer design for artists website and gallery

Current website is www.bluemoorstudio.com.au and it runs on a very simple Wordpress standard theme. We would like a theme designed and customised to suit the branding and style. We have someone who will then code the site in HTML and CSS into Wordpress.

The general theme and branding can be seen on the site at the moment. Please note I have now uploaded full size files into the project. The website background files are for reference only as they are currently on the site. There is no requirement to use them in the new design, however the logo must be as per the attachment.. Please submit a home page/main gallery, and we will request additional pages (about us, other galleries etc.) from those designers we like during the project time.
Updates

Please note I have now uploaded full size files into the project. The website background files are for reference only as they are currently on the site. There is no requirement to use them in the new design, however the logo must be as per the attachment.

Target Market(s)

sales are only in Australia, and priced between approx $100 and $1000. Most viewers and buyers are 20-40 years old, and looking for a casual canvas work for home, or a gift.

Industry/Entity Type

Artists

Font styles to use
Serif
Sans Serif

Requirements
Must have
• gallery of images, responsive design, ability to select categories of pictures (see top menu on current site) and have the gallery change to match, colours to match branding and logo.
Nice to have
• simple minimalist style is preferred. More like http://www.tobiasmerrow.com/ than http://www.harbourpaintco.com.au/ or http://www.velvetcanvas.com.au/
Should not have
• does not need any online store, or shopping cart etc.

```html
<!DOCTYPE html>
<html lang="en">
<head>
<meta charset="utf-8">
<title>Bluemoor Studio – Seascapes</title>
<link href="https://fonts.googleapis.com/css2?family=Open+Sans:wght@400;700&family=Lato:wght@400;700&display=swap" rel="stylesheet">
<style>
  :root {
    --ink: #111111;
    --brand-yellow: #f2e41b;
    --panel: #eeeeee;
    --rule: #dddddd;
    --muted: #b9b9b9;
    --artwork-tone: #c98a3e;
  }
  * { box-sizing: border-box; margin: 0; padding: 0; }
  html, body { width: 1200px; height: 1043px; overflow: hidden; background: #fff; }
  body { position: relative; font-family: "Open Sans", sans-serif; color: var(--ink); }

  .brand {
    position: absolute; top: 36px; left: 0; width: 1200px;
    display: flex; justify-content: center; align-items: center; gap: 8px;
    font-family: "Open Sans", sans-serif; font-weight: 700; font-size: 18px; letter-spacing: 0.5px;
  }
  .brand-square { width: 14px; height: 14px; background: var(--brand-yellow); }

  .social-top { position: absolute; top: 14px; left: 958px; display: flex; gap: 4px; }
  .social-dot { width: 19px; height: 19px; border: 1.5px solid var(--ink); border-radius: 50%; }

  .search {
    position: absolute; top: 58px; left: 838px; width: 162px; height: 23px;
    border: 1px solid #d6d6d6; background: #fff;
  }
  .search-button {
    position: absolute; right: 0; top: 0; width: 20px; height: 21px;
    border-left: 1px solid #d6d6d6; display: flex; align-items: center; justify-content: center;
  }

  .main-nav, .footer-nav {
    position: absolute; left: 0; width: 1200px;
    display: flex; justify-content: center; gap: 24px;
    font-size: 11.5px; text-transform: uppercase; list-style: none;
  }
  .main-nav { top: 117px; }
  .main-nav .is-active { color: var(--brand-yellow); }
  .footer-nav { top: 901px; color: var(--muted); }

  .header-rule { position: absolute; top: 144px; left: 0; width: 1200px; height: 1px; background: var(--rule); }

  .page-title {
    position: absolute; top: 170px; left: 200px;
    font-size: 30px; font-weight: 700; line-height: 1;
    padding-bottom: 8px; border-bottom: 6px solid var(--brand-yellow);
  }

  .gallery-bar { position: absolute; left: 199px; width: 801px; height: 7px; background: var(--ink); }
  .gallery-bar.top { top: 251px; }
  .gallery-bar.bottom { top: 640px; }
  .gallery-stage { position: absolute; top: 265px; left: 199px; width: 801px; height: 366px; background: var(--panel); }

  .artwork {
    position: absolute; top: 327px; left: 238px; width: 720px; height: 243px; overflow: hidden;
    background: var(--artwork-tone);
  }
  .sold-badge { position: absolute; left: 0; bottom: 0; width: 91px; height: 91px; }

  .pager { position: absolute; top: 673px; left: 533px; width: 134px; height: 27px; }

  .feedback-row {
    position: absolute; top: 771px; left: 0; width: 1200px; height: 40px;
    border-top: 1px solid var(--rule); border-bottom: 1px solid var(--rule);
    font-family: "Lato", sans-serif; font-weight: 700; font-size: 12.5px;
  }
  .feedback-row .label { position: absolute; top: 12px; }
  .rate { left: 201px; }
  .stars { position: absolute; top: 11px; left: 264px; }
  .share { left: 466px; }
  .share-buttons { position: absolute; top: 10px; left: 548px; display: flex; gap: 5px; }
  .share-button {
    font-family: "Open Sans", sans-serif; font-weight: 400; font-size: 9px; color: #444;
    border: 1px solid #d0d0d0; background: #f7f7f7; height: 17px; padding: 0 4px;
    display: flex; align-items: center; gap: 4px;
  }
  .share-button::before { content: ""; width: 10px; height: 10px; background: #9aa7b8; }
  .like { left: 868px; }
  .like-icons { position: absolute; top: 14px; left: 935px; display: flex; gap: 14px; }
  .like-dot { width: 12px; height: 12px; border-radius: 50%; background: #5f86b8; }

  .footer-divider { position: absolute; top: 840px; left: 0; }

  .copyright { position: absolute; top: 950px; left: 0; width: 1220px; text-align: center; font-size: 10px; color: #555; font-family: "Lato", sans-serif; }

  .footer-brand {
    position: absolute; top: 952px; left: 896px; width: 130px;
    display: flex; align-items: center; justify-content: center; gap: 6px;
    font-weight: 700; font-size: 13px;
  }
  .footer-brand .brand-square { width: 10px; height: 10px; background: var(--ink); }
  .footer-social { position: absolute; top: 1010px; left: 940px; display: flex; gap: 8px; }
  .footer-social span { width: 12px; height: 12px; border-radius: 50%; background: #555; }
</style>
</head>
<body>
  <header>
    <div class="brand"><span class="brand-square"></span>Bluemoor Studio</div>
    <div class="social-top"><span class="social-dot"></span><span class="social-dot"></span></div>
    <div class="search">
      <span class="search-button">
        <svg width="10" height="10" viewBox="0 0 10 10"><circle cx="4" cy="4" r="3" fill="none" stroke="#111" stroke-width="1.2"/><line x1="6.2" y1="6.2" x2="9.2" y2="9.2" stroke="#111" stroke-width="1.2"/></svg>
      </span>
    </div>
    <ul class="main-nav">
      <li>Home</li><li>About</li><li>Cityscapes</li><li>Other Works</li>
      <li class="is-active">Seacapes</li><li>Testimonials</li><li>Work for Sale</li>
    </ul>
    <div class="header-rule"></div>
  </header>

  <main>
    <h1 class="page-title">Seascapes</h1>
    <div class="gallery-bar top"></div>
    <div class="gallery-stage"></div>
    <div class="artwork" role="img" aria-label="Painting of a row of colourful beach huts on sand under a blue sky">
      <svg class="sold-badge" viewBox="0 0 91 91" aria-label="Sold for $248">
        <polygon points="0,0 0,91 91,91" fill="#f2e41b"/>
        <g transform="translate(28,60) rotate(45)" font-family="Open Sans, sans-serif" font-weight="700" font-size="13" fill="#111" text-anchor="middle">
          <text x="0" y="-13" dominant-baseline="central">SOLD</text>
          <text x="0" y="0" dominant-baseline="central">$</text>
          <text x="0" y="13" dominant-baseline="central">248</text>
        </g>
      </svg>
    </div>
    <div class="gallery-bar bottom"></div>

    <svg class="pager" viewBox="0 0 134 27" aria-label="Gallery navigation">
      <circle cx="13" cy="13.5" r="12.5" fill="#f2e41b" stroke="#c9bd10"/>
      <polyline points="16,7 10,13.5 16,20" fill="none" stroke="#111" stroke-width="1.8"/>
      <circle cx="43" cy="13.5" r="7" fill="#111"/>
      <circle cx="67" cy="13.5" r="7" fill="#111"/>
      <circle cx="91" cy="13.5" r="7" fill="#111"/>
      <circle cx="121" cy="13.5" r="12.5" fill="#f2e41b" stroke="#c9bd10"/>
      <polyline points="118,7 124,13.5 118,20" fill="none" stroke="#111" stroke-width="1.8"/>
    </svg>

    <section class="feedback-row">
      <span class="label rate">Rate this:</span>
      <svg class="stars" width="76" height="18" viewBox="0 0 76 18">
        <defs><polygon id="star" points="9,0 11.2,6.3 18,6.5 12.6,10.6 14.6,17 9,13.2 3.4,17 5.4,10.6 0,6.5 6.8,6.3"/></defs>
        <use href="#star" x="0" fill="#f2e41b"/>
        <use href="#star" x="19" fill="#f2e41b"/>
        <use href="#star" x="38" fill="#f2e41b"/>
        <use href="#star" x="57" fill="#111"/>
      </svg>
      <span class="label share">Share this:</span>
      <div class="share-buttons">
        <span class="share-button">Birdline</span>
        <span class="share-button">Pagebook</span>
        <span class="share-button">Searchly</span>
      </div>
      <span class="label like">Like this:</span>
      <div class="like-icons"><span class="like-dot"></span><span class="like-dot"></span></div>
    </section>
  </main>

  <footer>
    <svg class="footer-divider" width="1200" height="32" viewBox="0 0 1200 32">
      <polyline points="0,10 578,10 600,30 622,10 1200,10" fill="none" stroke="#dddddd" stroke-width="1.2" stroke-dasharray="6 4"/>
    </svg>
    <ul class="footer-nav">
      <li>Home</li><li>About</li><li>Cityscapes</li><li>Other Works</li>
      <li>Seacapes</li><li>Testimonials</li><li>Work for Sale</li>
    </ul>
    <p class="copyright">© Copyright Bluemoor Studio 2014</p>
    <div class="footer-brand"><span class="brand-square"></span>Bluemoor Studio</div>
    <div class="footer-social"><span></span><span></span><span></span></div>
  </footer>
</body>
</html>
```